business cards foreign exchange student company
Bluebird Hosting
Bright & Fun-filled
Mack Dorran
Service Director
Western Region
mack@mybluebirdhosting.com
mybluebirdhosting.com
This business card needs to be unforgettable! It needs to stand out from all the other business cards. Something clever/funny. It needs to communicate this is fun!! this is exciting!! and our theme for our company is "The Best Time Ever!" so the business card should convey that they have just found The Best Time Ever!!!
This will be my new website (with the old logo)
this is a marketing piece used to send families to the website
another marketing piece to get families to the website
This is my logo .ai file
This is my .ai logo file for dark backgrounds

```html
<!DOCTYPE html>
<html lang="en">
<head>
<meta charset="utf-8">
<title>Bluebird Hosting – Business Card Templates</title>
<link href="https://fonts.googleapis.com/css2?family=Arimo:ital,wght@0,400;0,700;1,700&display=swap" rel="stylesheet">
<style>
  :root {
    --board: #f3f3f3;
    --card-white: #ffffff;
    --card-grey: #d6d6d6;
    --accent-yellow: #ffd21f;
    --accent-red: #d8231f;
    --ink: #222222;
    --logo-ink: #1a4f8a;
  }
  * { margin: 0; padding: 0; box-sizing: border-box; }
  html, body { width: 1200px; height: 866px; overflow: hidden; background: var(--board); }
  body { position: relative; font-family: "Arimo", Arial, sans-serif; color: var(--ink); }

  .label {
    position: absolute; width: 437px; text-align: center;
    font-size: 25px; font-weight: 400; color: var(--ink);
  }

  .card {
    position: absolute; width: 437px; height: 300px; overflow: hidden;
    background: radial-gradient(ellipse at 30% 45%, var(--card-white) 35%, var(--card-grey) 100%);
    box-shadow: 0 4px 10px rgba(0,0,0,0.35);
  }
  .card .art { position: absolute; inset: 0; width: 437px; height: 300px; }

  .photo { position: absolute; }
  .photo--woman { left: 70px; top: 50px; width: 160px; height: 215px;
    background: radial-gradient(ellipse at 50% 40%, #e9c9b4 0%, #9c8d86 45%, rgba(230,230,230,0) 72%); }
  .photo--kids { left: 0; top: 95px; width: 200px; height: 170px;
    background: radial-gradient(ellipse at 45% 50%, #d99a7c 0%, #8a5a4a 40%, rgba(235,235,235,0) 72%); }
  .photo--girl { left: 10px; top: 58px; width: 200px; height: 208px;
    background: radial-gradient(ellipse at 45% 45%, #f0d2b6 0%, #a9b483 45%, rgba(235,235,235,0) 75%); }

  .logo { position: absolute; left: 12px; top: 12px; display: flex; align-items: center; gap: 5px; }
  .logo-mark { width: 18px; height: 18px; border-radius: 50%; background: var(--logo-ink); }
  .logo-name { font-size: 14px; font-weight: 700; color: var(--logo-ink); }

  .contact { position: absolute; left: 244px; top: 34px; width: 180px; color: var(--card-white); }
  .contact-name { font-size: 26px; font-weight: 400; line-height: 1.1; white-space: nowrap; }
  .contact-role { font-size: 13px; color: var(--accent-yellow); margin-top: 2px; }
  .contact-lines { margin-top: 10px; font-size: 8.5px; line-height: 1.35; white-space: nowrap; }
  .contact-lines .key { color: var(--accent-yellow); font-size: 6.5px; display: block; }

  .tagline { position: absolute; left: 22px; top: 274px; font-size: 18px; font-weight: 700;
    font-style: italic; color: var(--card-white); white-space: nowrap; }
  .tollfree { position: absolute; right: 12px; top: 234px; font-size: 12px; font-weight: 700;
    color: var(--accent-yellow); white-space: nowrap; }
  .tollfree .number { font-size: 17px; }
  .website { position: absolute; right: 12px; top: 256px; font-size: 10.5px; font-weight: 700;
    color: var(--accent-red); white-space: nowrap; }
</style>
</head>
<body>

<div class="label" style="left:96px; top:84px;">Blank Template</div>
<div class="label" style="left:624px; top:84px;">Template + Image sample</div>
<div class="label" style="left:96px; top:461px;">Template + Image sample</div>
<div class="label" style="left:624px; top:461px;">Template + Image sample</div>

<svg width="0" height="0" style="position:absolute">
  <defs>
    <linearGradient id="ribbonFill" x1="0" y1="0" x2="1" y2="1">
      <stop offset="0" stop-color="#5cc6f0"/>
      <stop offset="1" stop-color="#1f9ad6"/>
    </linearGradient>
    <linearGradient id="bandFill" x1="0" y1="0" x2="0" y2="1">
      <stop offset="0" stop-color="#2b8fd0"/>
      <stop offset="1" stop-color="#0f4f86"/>
    </linearGradient>
    <g id="cardArt">
      <polygon points="200,50 238,36 238,170 216,180" fill="#1480b8"/>
      <polygon points="238,24 428,20 428,162 238,170" fill="url(#ribbonFill)"/>
      <polygon points="330,170 428,162 428,178" fill="#1480b8"/>
      <path d="M0,266 Q130,246 250,256 L437,252 L437,258 L260,262 Q130,254 0,272 Z" fill="#ffffff"/>
      <rect x="250" y="231" width="187" height="22" rx="3" fill="#0f4f86"/>
      <rect x="250" y="253" width="187" height="16" fill="#ffffff"/>
      <path d="M0,270 Q140,252 260,269 L437,269 L437,300 L0,300 Z" fill="url(#bandFill)"/>
    </g>
  </defs>
</svg>

<div class="card" style="left:96px; top:127px;">
  <svg class="art" viewBox="0 0 437 300"><use href="#cardArt"/></svg>
  <div class="logo"><span class="logo-mark"></span><span class="logo-name">Bluebird Hosting</span></div>
  <div class="contact">
    <div class="contact-name">Mack Dorran</div>
    <div class="contact-role">Service Director</div>
    <div class="contact-lines"><span class="key">Email</span>mack@mybluebirdhosting.com<span class="key">Office</span>8015550142<span class="key">Cell</span>18015550187</div>
  </div>
  <div class="tollfree">Toll free: <span class="number">8775550199</span></div>
  <div class="website">www.mybluebirdhosting.com</div>
  <div class="tagline">Share The Adventure</div>
</div>

<div class="card" style="left:624px; top:127px;">
  <div class="photo photo--woman" role="img" aria-label="Photo of a laughing woman holding wrapped gifts"></div>
  <svg class="art" viewBox="0 0 437 300"><use href="#cardArt"/></svg>
  <div class="logo"><span class="logo-mark"></span><span class="logo-name">Bluebird Hosting</span></div>
  <div class="contact">
    <div class="contact-name">Mack Dorran</div>
    <div class="contact-role">Service Director</div>
    <div class="contact-lines"><span class="key">Email</span>mack@mybluebirdhosting.com<span class="key">Office</span>8015550142<span class="key">Cell</span>18015550187</div>
  </div>
  <div class="tollfree">Toll free: <span class="number">8775550199</span></div>
  <div class="website">www.mybluebirdhosting.com</div>
  <div class="tagline">Share The Adventure</div>
</div>

<div class="card" style="left:96px; top:504px;">
  <div class="photo photo--kids" role="img" aria-label="Photo of three smiling children lying together"></div>
  <svg class="art" viewBox="0 0 437 300"><use href="#cardArt"/></svg>
  <div class="logo"><span class="logo-mark"></span><span class="logo-name">Bluebird Hosting</span></div>
  <div class="contact">
    <div class="contact-name">Mack Dorran</div>
    <div class="contact-role">Service Director</div>
    <div class="contact-lines"><span class="key">Email</span>mack@mybluebirdhosting.com<span class="key">Office</span>8015550142<span class="key">Cell</span>18015550187</div>
  </div>
  <div class="tollfree">Toll free: <span class="number">8775550199</span></div>
  <div class="website">www.mybluebirdhosting.com</div>
  <div class="tagline">Share The Adventure</div>
</div>

<div class="card" style="left:624px; top:504px;">
  <div class="photo photo--girl" role="img" aria-label="Photo of a smiling young girl outdoors"></div>
  <svg class="art" viewBox="0 0 437 300"><use href="#cardArt"/></svg>
  <div class="logo"><span class="logo-mark"></span><span class="logo-name">Bluebird Hosting</span></div>
  <div class="contact">
    <div class="contact-name">Mack Dorran</div>
    <div class="contact-role">Service Director</div>
    <div class="contact-lines"><span class="key">Email</span>mack@mybluebirdhosting.com<span class="key">Office</span>8015550142<span class="key">Cell</span>18015550187</div>
  </div>
  <div class="tollfree">Toll free: <span class="number">8775550199</span></div>
  <div class="website">www.mybluebirdhosting.com</div>
  <div class="tagline">Share The Adventure</div>
</div>

</body>
</html>
```